Help design website for "Verdant Harbor Advisory" to advance the common good

Here is the Google doc link that lays out the design:

https://files.quillmarsh.net/doc/7TrWbnQe48XkLpZa2uMvYcD0sHfGjR35NwoEi9KxyBt/view?mode=share

Here is the Google drive folder with the logos and photos: https://store.quillmarsh.net/open?id=4K9pRtLmWqZx8825BvNcUaYeHs3Jd

The testimonials are being gathered and will be shared by Friday, 1/4.

The winner will also have to migrate the coding files to my hosting site.

Thank you for your help! Looking forward to seeing your designs.

Target Market(s)

Prospective clients

Industry/Entity Type

Non Profit

Coding

Coded - Design and coding required

Number of Pages Required

5+ page

Requirements
Must have
• Noted in the Google doc regarding layout.
Nice to have

```html
<!DOCTYPE html>
<html lang="en">
<head>
<meta charset="utf-8">
<title>Verdant Harbor Advisory — Services &amp; Testimonials</title>
<link href="https://fonts.googleapis.com/css2?family=Jost:wght@300;400;600&family=Poppins:wght@400;500&display=swap" rel="stylesheet">
<style>
  :root {
    --ink-dark: #30333f;
    --brand-blue: #2b9ae3;
    --page-light: #f7f9fc;
    --frame-grey: #5b5e63;
    --text-dark: #2a2c33;
    --white: #ffffff;
  }
  * { margin: 0; padding: 0; box-sizing: border-box; }
  html, body { width: 1200px; height: 945px; overflow: hidden; }
  body { font-family: "Poppins", sans-serif; background: var(--page-light); color: var(--text-dark); }

  .site-header {
    height: 160px; background: var(--ink-dark);
    display: flex; align-items: center; justify-content: center; gap: 18px;
  }
  .brand-mark { width: 26px; height: 26px; background: var(--brand-blue); }
  .brand-name {
    font-family: "Jost", sans-serif; font-weight: 400; font-size: 30px;
    letter-spacing: 7px; color: var(--white); text-transform: uppercase;
  }

  .main-nav {
    height: 30px; background: var(--brand-blue);
    display: flex; justify-content: center; align-items: center; gap: 26px;
  }
  .main-nav a {
    font-size: 10px; color: var(--white); text-decoration: none; text-transform: uppercase;
  }
  .main-nav a.is-current { color: var(--ink-dark); }

  .development {
    height: 473px; padding-top: 34px; text-align: center;
  }
  .section-title {
    font-family: "Jost", sans-serif; font-size: 24px; font-weight: 300;
    color: var(--text-dark); letter-spacing: 0.5px;
  }
  .section-title strong { font-weight: 600; color: var(--brand-blue); }
  .gallery {
    display: flex; justify-content: center; gap: 24px; margin-top: 34px;
  }
  .gallery-item { width: 362px; }
  .photo {
    width: 362px; height: 293px; border: 4px solid var(--frame-grey);
  }
  .photo--reception { background: linear-gradient(160deg, #8a7a68 0%, #3b2e2a 55%, #1f1a1c 100%); }
  .photo--celebration { background: linear-gradient(170deg, #c9c2b8 0%, #7d5b4f 50%, #3a3440 100%); }
  .caption {
    margin-top: 24px; font-size: 12.4px; line-height: 15.5px; color: var(--brand-blue);
  }

  .testimonial {
    height: 250px; background: var(--ink-dark); text-align: center; padding-top: 25px;
  }
  .testimonial-title {
    font-family: "Jost", sans-serif; font-weight: 600; font-size: 25px;
    color: var(--brand-blue); letter-spacing: 0.5px;
  }
  .quote {
    width: 640px; margin: 43px auto 0; font-size: 9.4px; line-height: 14px; color: var(--white);
  }
  .attribution {
    margin-top: 29px; font-size: 12px; font-weight: 500; color: var(--white);
  }
  .attribution .person { color: var(--brand-blue); font-weight: 400; }
  .slider-dots { display: flex; justify-content: center; gap: 4px; margin-top: 18px; }
  .slider-dots span { width: 9px; height: 9px; border-radius: 50%; background: var(--brand-blue); }
  .slider-dots span.is-active { background: var(--white); }

  .site-footer {
    height: 32px; background: var(--brand-blue);
    display: flex; align-items: center; justify-content: center;
    font-size: 9.5px; color: var(--white);
  }
</style>
</head>
<body>
  <header class="site-header">
    <span class="brand-mark"></span>
    <span class="brand-name">Verdant Harbor Advisory</span>
  </header>

  <nav class="main-nav">
    <a href="#">Home</a>
    <a href="#" class="is-current">Services &amp; Testimonials</a>
    <a href="#">Media &amp; Impact</a>
    <a href="#">Contact</a>
  </nav>

  <section class="development">
    <h1 class="section-title">STAFF <strong>PROFESSIONAL DEVELOPMENT</strong></h1>
    <div class="gallery">
      <figure class="gallery-item">
        <div class="photo photo--reception" role="img" aria-label="Group photo of Nora and her staff team holding colourful signs at an awards reception"></div>
        <figcaption class="caption">Nora with Her Staff Team at Their<br>Annual Community Impact Awards Reception</figcaption>
      </figure>
      <figure class="gallery-item">
        <div class="photo photo--celebration" role="img" aria-label="Smiling group selfie of Nora's staff team at an end-of-year celebration"></div>
        <figcaption class="caption">Nora with Her Staff Team at their End-of-School<br>Year Meeting and Celebration</figcaption>
      </figure>
    </div>
  </section>

  <section class="testimonial">
    <h2 class="testimonial-title">TESTIMONIAL</h2>
    <p class="quote">"Aenean quis nisl mi. Proin quis orci et neque vehicula maximus. Curabitur libero elit, vestibulum sit amet sodales ut, placerat ac tortor. Phasellus eget tincidunt metus. Maecenas et augue eu sapien interdum molestie. Vestibulum efficitur sodales velit. Aliquam erat volutpat. Quisque nunc dolor, maximus eget turpis ac, imperdiet iaculis urna."</p>
    <p class="attribution"><span class="person">Dorian Feld,</span> Chief Executive Officer, Fairpath Collective</p>
    <div class="slider-dots"><span class="is-active"></span><span></span></div>
  </section>

  <footer class="site-footer">© 2019, All Rights Reserved, Verdant Harbor Advisory</footer>
</body>
</html>
```